Law Firm
To All Designers:
New e-mail address for the project is daniel@rvestlegal.net.
Thanks. I love all the designs.
P.S. I like the orange on the one side of the card as opposed to black.
@ph - New drafts #161 & #162 in lieu of 145 & 146 are submitted, Can you please check & provide feedback in private message.
Thanks
draft #145 and #146 Drafts came out black and I cannot see them (look like negatives). Please resubmit. Thanks.
Please DO NOT PUT "Gavels", "Scales of Justice" "Court Buildings", etc. on the card. I DO NOT WANT IT.
Thanks.
draft #130 Card looks a lot better. Can I see it with the dot at the end of the big line through the card a little smaller (but that is the look I was going for) and can I see some color (black, orange and/or grey) below that line where the address, phone and e-mail appear? Also, can I see with just the "m" and the line part of the logo on the other side? Thanks.
draft #125 and #126 Looks better. I didn't like the "watermark" "m" in my logo being sideways on the card (it didn't look like an "m" anymore to me that way), but Ido like it on the stationary and envelope. Can I see the card with the same orange on the one side with the orange line under the "m" in my logo at the bottom of the card then the address, telephone and e-mail below it? Thanks.
To all designers,
Can I start seeing letterhead, envelopes, fax covers and e-mail signatures too! I look forward to seeing the designs!
draft #49 I like the line under my name like in the logo. Can I see with orange on the other side of the card?
drafts #101, #102, #103 and #104 I would like to see with orange on the other side of the card rather than black
I like the use of the whites and oranges with black accents. So not too much black. I also like orange with the logo (either with the text or just the script "m") on one side of the card. Thanks for all the great designs.
draft #35 I like the use of the logo at the bottom of the card. But "no "scales of justice", "court buildings" or "gavels", etc. was not something I wanted on the card, it was just an instruction to the designers that although I am a lawyer, I do not want to use these symbols.
draft #31 and #32 Maybe you could use the orange line under the script "m" under the logo for the "white space"?
draft #31 and #32 Like the use of the colors in the card and the "watermark" logo on the stationary. However, there is too much "white space" on the right side of the card. Other drafts did better job with "white space". I would also like to maybe see the "watermark" logo used in the card as well.

```html
<!DOCTYPE html>
<html lang="en">
<head>
<meta charset="utf-8">
<title>Daniel R. Vest, P.C. — Business Card</title>
<link href="https://fonts.googleapis.com/css2?family=Cinzel:wght@500&family=Libre+Baskerville&display=swap" rel="stylesheet">
<style>
  :root {
    --backdrop: #e9e6e1;
    --card: #ffffff;
    --ink: #1d1d1d;
    --orange: #f26a2e;
    --grey: #6d6d6d;
    --rule: #cfcfcf;
  }
  * { box-sizing: border-box; margin: 0; padding: 0; }
  html, body { width: 1200px; height: 646px; overflow: hidden; }
  body {
    background: var(--backdrop);
    font-family: "Libre Baskerville", Georgia, serif;
    color: var(--ink);
    position: relative;
  }
  .card {
    position: absolute;
    top: 174px;
    width: 520px;
    height: 297px;
    background: var(--card);
    box-shadow: 0 6px 18px rgba(0,0,0,.12);
    overflow: hidden;
  }
  .card--back { left: 50px; }
  .card--front { left: 630px; }

  .wordmark {
    position: absolute;
    left: 0; right: 0;
    text-align: center;
    font-family: "Cinzel", serif;
    font-weight: 500;
    color: var(--ink);
  }
  .wordmark__name { font-size: 27px; letter-spacing: 1px; line-height: 1; }
  .wordmark__tag { font-size: 11px; letter-spacing: 4px; margin-top: 7px; color: var(--grey); }
  .card--back .wordmark { top: 118px; }
  .card--front .wordmark { top: 48px; }

  .wordmark-rule {
    position: absolute;
    left: 150px;
    width: 220px;
    height: 2px;
    background: linear-gradient(90deg, transparent, var(--orange) 20%, var(--orange) 80%, transparent);
  }
  .card--back .wordmark-rule { top: 186px; }
  .card--front .wordmark-rule { top: 116px; }

  .holder {
    position: absolute;
    top: 132px;
    left: 44px;
    width: 180px;
    text-align: right;
  }
  .holder__name { color: var(--orange); font-size: 15px; }
  .holder__role { color: var(--grey); font-size: 11px; margin-top: 6px; }

  .divider {
    position: absolute;
    top: 126px;
    left: 244px;
    width: 1px;
    height: 66px;
    background: var(--rule);
  }

  .contact {
    position: absolute;
    top: 126px;
    left: 262px;
    list-style: none;
    font-size: 10.5px;
    color: var(--ink);
  }
  .contact li { display: flex; align-items: center; gap: 7px; height: 16px; }
  .contact li.no-icon { padding-left: 16px; }
  .contact svg { width: 9px; height: 9px; flex: none; }

  .base-rule {
    position: absolute;
    left: 0; right: 0;
    bottom: 52px;
    height: 1px;
    background: var(--ink);
  }
  .base-band {
    position: absolute;
    left: 0; right: 0;
    bottom: 0;
    height: 44px;
    background: var(--orange);
  }
</style>
</head>
<body>

  <section class="card card--back" aria-label="Card back">
    <div class="wordmark">
      <div class="wordmark__name">Daniel R. Vest, P.C.</div>
      <div class="wordmark__tag">Legal Consulting</div>
    </div>
    <div class="wordmark-rule"></div>
  </section>

  <section class="card card--front" aria-label="Card front">
    <div class="wordmark">
      <div class="wordmark__name">Daniel R. Vest, P.C.</div>
      <div class="wordmark__tag">Legal Consulting</div>
    </div>
    <div class="wordmark-rule"></div>

    <div class="holder">
      <p class="holder__name">Daniel R. Vest</p>
      <p class="holder__role">Principal</p>
    </div>

    <div class="divider"></div>

    <ul class="contact">
      <li class="no-icon">27 Harbor Lane</li>
      <li class="no-icon">Millbrook, NY 10034</li>
      <li>
        <svg viewBox="0 0 10 10"><rect width="10" height="10" rx="1.5" fill="var(--orange)"/><path d="M3 2.5c0 3 1.5 4.5 4.5 5l.5-1.2-1.4-.6-.6.6C5 5.7 4.3 5 3.7 4l.6-.6-.6-1.4z" fill="#fff"/></svg>
        (555) 204-7731
      </li>
      <li>
        <svg viewBox="0 0 10 10"><rect width="10" height="10" rx="1.5" fill="var(--orange)"/><rect x="2" y="3" width="6" height="4" fill="none" stroke="#fff" stroke-width=".8"/><path d="M2 3l3 2.3L8 3" fill="none" stroke="#fff" stroke-width=".8"/></svg>
        daniel@rvestlegal.net
      </li>
    </ul>

    <div class="base-rule"></div>
    <div class="base-band"></div>
  </section>

</body>
</html>
```